Visual design for database driven web application

Need a clean, professional looking visual design for a web application.

PLUME is the new standardized K-12 school testing program for the state of Texas. We are building an application named PLUME-Finder (clever, yeah?) that will allow teachers, school administrators, and others to EASILY sort through millions of records of student data and print or export reports showing just the information they need about their students.

The state currently doesn't provide a user-friendly way to do this. They provide a "data dump" spreadsheet that school administrators and teachers must figure out how to manipulate to get the data they need. We are building a Web-based tool that will make it super simple and easy for our users to get the data they need in a format that works for them.

I've created a basic wireframe of the main application screen in Vellum QD Max. I need you to "skin" the wireframe to make it look good. Your mockup will set the tone for branding and visual design throughout the site.

See the attached screenshots. There are a few variations of the screen that include dynamic panels that open & close. Start by designing just the main screen and if you have time, do one or two of the panels. Thanks!
Updates

Target Market(s)

K-12 education professionals (teachers, administrators) in the state of Texas

Industry/Entity Type

Building

Requirements
Must have
• Your mockups should include all of the features & content shown in the attached screenshots.

However, you don't have to show all 10 rows of data. You can just do the column headers and one row of data. (It would be repetitive and unnecessary to spend time re-creating the entire grid with all of that data just to show your visual styling.)

The design should reflect the following concepts:

- Texas
- Education
- Simplicity
- Helpfulness
- Trust
- Professionalism

If I select your design, I will want your design source files (Illustrator, Photoshop, etc.)
Nice to have
• A logo in the upper left corner for PLUME-Finder. The logo should definitely communicate the design concepts described under "must have."

```html
<!DOCTYPE html>
<html lang="en">
<head>
<meta charset="utf-8">
<title>PLUME-Finder – Students Data</title>
<link href="https://fonts.googleapis.com/css2?family=Arimo&family=PT+Sans:wght@400;700&family=Montserrat:wght@700&display=swap" rel="stylesheet">
<style>
:root{
  --slate:#4a5f6a;
  --slate-dark:#3c4d56;
  --sand:#d0cfbf;
  --page:#efefef;
  --panel:#f3f3f3;
  --text:#4b5a63;
  --ink:#222;
  --row-a:#f6f6f6;
  --row-b:#e5e6e7;
  --line:#c9c9c9;
  --alert:#d4262b;
  --orange:#f39200;
}
*{box-sizing:border-box;margin:0;padding:0}
html,body{width:1200px;height:1125px;overflow:hidden}
body{background:var(--page);font-family:"PT Sans",sans-serif;color:var(--text);position:relative}
.header{position:absolute;left:0;top:0;width:1200px;height:186px;background:#fff}
.brand{position:absolute;left:26px;top:10px;font-family:"Montserrat",sans-serif;font-weight:700;font-size:31px;color:var(--slate);letter-spacing:-1px}
.account{position:absolute;left:915px;top:0;width:257px;height:31px;background:#ebebeb;font-size:13px;display:flex;align-items:center;padding-left:17px;gap:22px}
.account .welcome{color:#333;font-size:14px}
.account .links{color:#7a8890}
.search{position:absolute;left:423px;top:70px;display:flex}
.search input{width:278px;height:32px;border:1px solid #d4d4d4;border-radius:5px 0 0 5px;background:#fff}
.search button{width:112px;height:32px;border:none;border-radius:0 5px 5px 0;background:linear-gradient(#5b6f79,#3e505a);color:#fff;font:16px "PT Sans",sans-serif;display:flex;align-items:center;justify-content:center;gap:8px}
.search-options{position:absolute;left:700px;top:107px;font-size:15px;color:var(--text)}
.tabs{position:absolute;left:26px;top:149px;display:flex;gap:8px}
.tab{width:192px;height:37px;border-radius:4px 4px 0 0;font-size:19px;display:flex;align-items:center;justify-content:center}
.tab.active{background:var(--slate);color:#fff}
.tab.inactive{background:var(--sand);color:var(--slate)}
.band{position:absolute;left:0;top:186px;width:1200px;height:13px;background:var(--slate)}
.panel{position:absolute;left:0;top:199px;width:1200px;height:670px;background:var(--panel)}
.toolbar{position:absolute;left:27px;top:225px;display:flex;align-items:center;font-size:15px}
.toggle{margin-left:8px;background:#a9a9a9;color:#fff;border-radius:3px;padding:2px 10px;font-size:15px}
.filtered{margin-left:28px}
.filtered a{color:var(--alert)}
.export{position:absolute;right:28px;top:226px;font-size:15px;color:#8a969c;display:flex;gap:12px;align-items:center}
.pager{position:absolute;left:27px;display:flex;align-items:center;font-family:Georgia,serif;font-size:14px;color:var(--text)}
.pager .btn{height:19px;border:1px solid #b8b8b8;background:#f7f7f7;padding:0 6px;line-height:17px;margin-right:6px}
.pager .wide{width:76px;margin-right:14px}
.pager .next{width:76px;margin-left:0}
.pager .num{width:23px;text-align:center;padding:0}
.pager .num.current{background:var(--slate);color:#fff;border-color:var(--slate)}
.pager .dots{width:80px;margin:0 6px 0 4px;letter-spacing:1px}
.pager .rows{margin-left:42px;font-family:"PT Sans",sans-serif;font-size:15px;display:flex;align-items:center;gap:8px}
.pager select{font:14px Georgia,serif;height:19px;border:1px solid #b8b8b8;background:#f7f7f7;color:var(--text);width:40px}
table.data{position:absolute;left:27px;top:341px;width:1146px;border-collapse:collapse;border:1px solid #aaa;font-family:"Arimo",sans-serif;font-size:15px;color:var(--ink)}
table.data th{background:#e8e8e8;font-weight:400;text-align:left;height:33px;padding-left:5px;border-right:1px solid var(--line)}
table.data td{height:34px;padding-left:6px;border-right:1px solid var(--line)}
table.data tbody tr:nth-child(odd){background:var(--row-a)}
table.data tbody tr:nth-child(even){background:var(--row-b)}
</style>
</head>
<body>
<header class="header">
  <div class="brand">PLUME-Finder</div>
  <div class="account"><span class="welcome">Welcome, Dana</span><span class="links">my profile &nbsp;| &nbsp;log out</span></div>
  <form class="search">
    <input type="text" aria-label="Search">
    <button type="button"><svg width="20" height="20" viewBox="0 0 20 20"><circle cx="8" cy="8" r="5.5" fill="none" stroke="#fff" stroke-width="2"/><line x1="12" y1="12" x2="18" y2="18" stroke="#fff" stroke-width="3"/></svg>Search</button>
  </form>
  <div class="search-options">search options <svg width="8" height="5"><path d="M0 0h8L4 5z" fill="#4b5a63"/></svg></div>
  <nav class="tabs"><div class="tab active">Instructions</div><div class="tab inactive">Students Data</div></nav>
</header>
<div class="band"></div>
<main class="panel"></main>

<div class="toolbar">Showing 26 of 38 columns <span class="toggle">▾ &nbsp;Show / Hide</span><span class="filtered">3 columns are <a href="#">filtered</a></span></div>
<div class="export"><span>🖶 print</span><span style="color:#ccc">|</span><span>⤓ download</span></div>

<div class="pager" style="top:290px">
  <span class="btn wide">« Previous</span>
  <span class="btn num current">1</span><span class="btn num">2</span><span class="btn num">3</span><span class="btn num">4</span><span class="btn num">5</span>
  <span class="dots">..................</span>
  <span class="btn num">12</span><span class="btn num">13</span>
  <span class="btn next">&nbsp;&nbsp;Next »</span>
  <span class="rows">Show <select aria-label="rows"><option>10</option></select> rows per page</span>
</div>

<table class="data">
  <colgroup><col style="width:88px"><col style="width:69px"><col style="width:74px"><col style="width:107px"><col style="width:100px"><col style="width:121px"><col style="width:122px"><col style="width:122px"><col style="width:59px"><col style="width:93px"><col style="width:91px"><col style="width:100px"></colgroup>
  <thead><tr><th>Date</th><th>Grade</th><th>ESC</th><th>CDCD#</th><th>District</th><th>Campus</th><th>Last Name</th><th>First Name</th><th>MI</th><th>Student ID</th><th>Gender</th><th>DOB</th></tr></thead>
  <tbody>
    <tr><td>411</td><td>9</td><td>10</td><td>99990011#</td><td>EXAMPLE</td><td>EXAMPLE</td><td>EXAMPLE</td><td>EXAMPLE</td><td>10</td><td>10</td><td>MALE</td><td>10</td></tr>
    <tr><td>411</td><td>9</td><td>10</td><td>99990011#</td><td>EXAMPLE</td><td>EXAMPLE</td><td>EXAMPLE</td><td>EXAMPLE</td><td>10</td><td>10</td><td>MALE</td><td>10</td></tr>
    <tr><td>411</td><td>9</td><td>10</td><td>99990011#</td><td>EXAMPLE</td><td>EXAMPLE</td><td>EXAMPLE</td><td>EXAMPLE</td><td>10</td><td>10</td><td>MALE</td><td>10</td></tr>
    <tr><td>411</td><td>9</td><td>10</td><td>99990011#</td><td>EXAMPLE</td><td>EXAMPLE</td><td>EXAMPLE</td><td>EXAMPLE</td><td>10</td><td>10</td><td>MALE</td><td>10</td></tr>
    <tr><td>411</td><td>9</td><td>10</td><td>99990011#</td><td>EXAMPLE</td><td>EXAMPLE</td><td>EXAMPLE</td><td>EXAMPLE</td><td>10</td><td>10</td><td>MALE</td><td>10</td></tr>
    <tr><td>411</td><td>9</td><td>10</td><td>99990011#</td><td>EXAMPLE</td><td>EXAMPLE</td><td>EXAMPLE</td><td>EXAMPLE</td><td>10</td><td>10</td><td>MALE</td><td>10</td></tr>
    <tr><td>411</td><td>9</td><td>10</td><td>99990011#</td><td>EXAMPLE</td><td>EXAMPLE</td><td>EXAMPLE</td><td>EXAMPLE</td><td>10</td><td>10</td><td>MALE</td><td>10</td></tr>
    <tr><td>411</td><td>9</td><td>10</td><td>99990011#</td><td>EXAMPLE</td><td>EXAMPLE</td><td>EXAMPLE</td><td>EXAMPLE</td><td>10</td><td>10</td><td>MALE</td><td>10</td></tr>
    <tr><td>411</td><td>9</td><td>10</td><td>99990011#</td><td>EXAMPLE</td><td>EXAMPLE</td><td>EXAMPLE</td><td>EXAMPLE</td><td>10</td><td>10</td><td>MALE</td><td>10</td></tr>
    <tr><td>411</td><td>9</td><td>10</td><td>99990011#</td><td>EXAMPLE</td><td>EXAMPLE</td><td>EXAMPLE</td><td>EXAMPLE</td><td>10</td><td>10</td><td>MALE</td><td>10</td></tr>
  </tbody>
</table>

<div class="pager" style="top:745px">
  <span class="btn wide">« Previous</span>
  <span class="btn num current">1</span><span class="btn num">2</span><span class="btn num">3</span><span class="btn num">4</span><span class="btn num">5</span>
  <span class="dots">..................</span>
  <span class="btn num">12</span><span class="btn num">13</span>
  <span class="btn next">&nbsp;&nbsp;Next »</span>
  <span class="rows">Show <select aria-label="rows"><option>10</option></select> rows per page</span>
</div>
</body>
</html>
```